Real Estate developer

I am building a 55+ adult community and I need a business card
Information to be Included in the Business Card:
Company Name: Birch Hollow Estates, in my font
Tobin Fell
President
Phone: 207-555-0148
Address:
Birch Hollow Estates, LLC
9 Dunmore Lane,
Lewiston MAINE, 04240
Web Address: www.birchhollowestatesnorth.example
Target Market(s)
55 year and older home buyers
Industry/Entity Type
Building
Font styles to use
Other font styles liked:
- Boulevard BQ
Requirements
Must have
- This message must be on card: A 55+ Adult Community

```html
<!DOCTYPE html>
<html lang="en">
<head>
<meta charset="utf-8">
<title>Birch Hollow Estates – Business Card</title>
<link rel="stylesheet" href="https://fonts.googleapis.com/css2?family=Pinyon+Script&family=Alfa+Slab+One&family=Montserrat:wght@600;700&family=Arimo:wght@700&display=swap">
<style>
  :root {
    --card-bg: #dfe7ea;
    --card-bg-edge: #cfdadf;
    --brand-green: #3dbf6e;
    --tag-green: #4fd36a;
    --tag-outline: #1f6b35;
    --title-gold: #d6891c;
    --title-outline: #2a2418;
    --ink: #111111;
  }
  html, body {
    margin: 0;
    padding: 0;
    width: 1200px;
    height: 686px;
    overflow: hidden;
    background: var(--card-bg);
  }
  .card {
    position: relative;
    width: 1200px;
    height: 686px;
    background: radial-gradient(ellipse at center, #e8eef0 0%, var(--card-bg) 60%, var(--card-bg-edge) 100%);
    overflow: hidden;
  }
  .brand-mark {
    position: absolute;
    left: 66px;
    top: 46px;
    height: 96px;
    display: flex;
    align-items: center;
    gap: 14px;
  }
  .brand-mark__square {
    width: 26px;
    height: 26px;
    background: var(--brand-green);
    flex: none;
  }
  .brand-mark__name {
    font-family: "Montserrat", sans-serif;
    font-weight: 700;
    font-size: 29px;
    line-height: 1.15;
    color: var(--brand-green);
  }
  .contact-person {
    position: absolute;
    top: 54px;
    left: 953px;
    width: 200px;
    text-align: center;
    font-family: "Arimo", sans-serif;
    font-weight: 700;
    font-size: 24px;
    line-height: 1.3;
    color: var(--ink);
  }
  .company-title {
    position: absolute;
    left: 0;
    right: 0;
    top: 262px;
    margin: 0;
    text-align: center;
    font-family: "Pinyon Script", cursive;
    font-weight: 400;
    font-size: 86px;
    line-height: 1;
    color: var(--title-gold);
    -webkit-text-stroke: 1.8px var(--title-outline);
    text-shadow: 2px 2px 0 rgba(0,0,0,0.25);
  }
  .tagline {
    position: absolute;
    left: 0;
    right: 0;
    top: 394px;
    margin: 0;
    text-align: center;
    font-family: "Alfa Slab One", serif;
    font-size: 33px;
    line-height: 1.1;
    letter-spacing: 4px;
    word-spacing: 14px;
    color: var(--tag-green);
    -webkit-text-stroke: 1px var(--tag-outline);
    text-shadow: 0 0 2px #ffffff, 0 0 3px #ffffff;
  }
  .contact-details {
    position: absolute;
    left: 0;
    right: 0;
    top: 536px;
    margin: 0;
    text-align: center;
    font-family: "Montserrat", sans-serif;
    font-weight: 600;
    font-size: 28px;
    line-height: 33px;
    letter-spacing: 0.5px;
    color: var(--ink);
    font-style: normal;
  }
  .contact-details span { display: block; }
</style>
</head>
<body>
  <main class="card">
    <div class="brand-mark">
      <div class="brand-mark__square"></div>
      <div class="brand-mark__name">Birch Hollow<br>Estates</div>
    </div>

    <div class="contact-person">
      <div class="contact-person__name">Tobin Fell</div>
      <div class="contact-person__role">President</div>
    </div>

    <h1 class="company-title">Birch Hollow Estates</h1>
    <p class="tagline">A 55+ Adult Community</p>

    <address class="contact-details">
      <span class="contact-details__address">Address: 9 Dunmore Lane, Lewiston MAINE, 04240</span>
      <span class="contact-details__phone">Phone: 207-555-0148</span>
      <span class="contact-details__web">Website: www.birchhollowestatesnorth.example</span>
    </address>
  </main>
</body>
</html>
```